Looking for awesome business card design with attached existing logo

We are a water, mold, and fire damage restoration company called "Torvane Seco" Looking for an awesome business card that is edgy yet professional and unique. Show me what you got!

```html
<!DOCTYPE html>
<html lang="en">
<head>
<meta charset="utf-8">
<title>Torvane Seco — Business Card</title>
<link href="https://fonts.googleapis.com/css2?family=Montserrat:wght@400;500;700&display=swap" rel="stylesheet">
<style>
  :root {
    --bg: #3a3a3a;
    --teal: #0b4452;
    --teal-deep: #083c49;
    --orange: #e59b12;
    --white: #ffffff;
    --divider: rgba(255,255,255,0.45);
  }
  * { box-sizing: border-box; margin: 0; padding: 0; }
  html, body {
    width: 1200px; height: 1200px; overflow: hidden;
    background: var(--bg);
    font-family: "Montserrat", sans-serif;
  }
  .stage { position: relative; width: 1200px; height: 1200px; }

  .card {
    position: absolute;
    width: 780px; height: 460px;
    border-radius: 34px;
    overflow: hidden;
    box-shadow: 0 18px 40px rgba(0,0,0,0.45);
  }

  /* Front side */
  .card-front { left: 90px; top: 90px; background: var(--white); }
  .front-brand {
    position: absolute; left: 0; right: 0; top: 0; height: 240px;
    display: flex; align-items: center; justify-content: center; gap: 14px;
  }
  .brand-dot { width: 22px; height: 22px; border-radius: 50%; background: var(--orange); }
  .brand-name {
    font-weight: 700; font-size: 56px; letter-spacing: 1px;
    color: var(--teal); text-transform: uppercase;
  }
  .front-stripe {
    position: absolute; left: 0; right: 0; top: 252px; height: 8px;
    background: var(--orange);
  }
  .front-band {
    position: absolute; left: 0; right: 0; top: 268px; bottom: 0;
    background: var(--teal);
  }
  .holder {
    position: absolute; left: 60px; top: 66px;
    border-left: 6px solid var(--orange); padding-left: 14px;
  }
  .holder-name { font-weight: 500; font-size: 34px; color: var(--orange); line-height: 1; }
  .holder-role { font-weight: 400; font-size: 20px; color: var(--white); margin-top: 6px; letter-spacing: 0.5px; }
  .band-divider {
    position: absolute; left: 390px; top: 40px; width: 1px; height: 112px;
    background: var(--divider);
  }
  .contacts {
    position: absolute; left: 440px; top: 34px;
    list-style: none; display: flex; flex-direction: column; gap: 16px;
  }
  .contact {
    display: flex; align-items: center; gap: 12px;
    color: var(--white); font-size: 21px; font-weight: 400;
  }
  .contact svg { width: 24px; height: 24px; flex: none; }

  /* Back side */
  .card-back {
    left: 330px; top: 650px;
    background: linear-gradient(120deg, var(--teal-deep) 0%, var(--teal) 55%, #0e4a58 100%);
    display: flex; align-items: center; justify-content: center; gap: 20px;
  }
  .card-back .brand-name { color: var(--white); font-size: 78px; }
  .card-back .brand-dot { width: 30px; height: 30px; }
</style>
</head>
<body>
<main class="stage">

  <section class="card card-front">
    <div class="front-brand">
      <span class="brand-dot"></span>
      <span class="brand-name">Torvane Seco</span>
    </div>
    <div class="front-stripe"></div>
    <div class="front-band">
      <div class="holder">
        <p class="holder-name">JOHN DOE</p>
        <p class="holder-role">POSITION</p>
      </div>
      <div class="band-divider"></div>
      <ul class="contacts">
        <li class="contact">
          <svg viewBox="0 0 24 24" aria-hidden="true"><path fill="#e59b12" d="M6.6 10.8a15 15 0 0 0 6.6 6.6l2.2-2.2c.3-.3.7-.4 1-.2 1.1.4 2.3.6 3.6.6.6 0 1 .4 1 1V20c0 .6-.4 1-1 1A17 17 0 0 1 3 4c0-.6.4-1 1-1h3.5c.6 0 1 .4 1 1 0 1.3.2 2.5.6 3.6.1.3 0 .7-.2 1z"/></svg>
          (000) 000 0000
        </li>
        <li class="contact">
          <svg viewBox="0 0 24 24" aria-hidden="true"><rect x="2" y="5" width="20" height="14" rx="1" fill="#e59b12"/><path d="M2 6l10 7 10-7" fill="none" stroke="#0b4452" stroke-width="1.8"/></svg>
          email@torvaneseco.com
        </li>
        <li class="contact">
          <svg viewBox="0 0 24 24" aria-hidden="true"><g fill="none" stroke="#e59b12" stroke-width="1.8"><circle cx="12" cy="12" r="9.5"/><ellipse cx="12" cy="12" rx="4" ry="9.5"/><path d="M2.5 12h19M4 7h16M4 17h16"/></g></svg>
          www.torvaneseco.com
        </li>
      </ul>
    </div>
  </section>

  <section class="card card-back">
    <span class="brand-dot"></span>
    <span class="brand-name">Torvane Seco</span>
  </section>

</main>
</body>
</html>
```